BKA

Please send us some options for letterhead I attached our Logo. In addition to the Logo we need this information somewhere on the page

47 Fenbury Lane
Harlow Bay, ME 04231
203-481-7629

```html
<!DOCTYPE html>
<html lang="en">
<head>
<meta charset="utf-8">
<title>BKA Letterhead</title>
<link href="https://fonts.googleapis.com/css2?family=Roboto+Condensed:wght@500;700&display=swap" rel="stylesheet">
<style>
  :root {
    --brand-brown: #574a46;
    --ink: #1d1d1d;
    --paper: #ffffff;
  }
  * { margin: 0; padding: 0; box-sizing: border-box; }
  html, body {
    width: 848px;
    height: 1200px;
    overflow: hidden;
    background: var(--paper);
  }
  .letterhead {
    position: relative;
    width: 848px;
    height: 1200px;
    background: var(--paper);
    font-family: "Roboto Condensed", Arial, sans-serif;
  }
  .top-band {
    position: absolute;
    top: 0;
    left: 0;
    width: 848px;
    height: 114px;
  }
  .brand {
    position: absolute;
    top: 106px;
    left: 0;
    width: 100%;
    height: 60px;
    display: flex;
    justify-content: center;
    align-items: center;
    gap: 14px;
  }
  .brand-mark {
    width: 54px;
    height: 54px;
    background: var(--brand-brown);
  }
  .brand-name {
    font-weight: 700;
    font-size: 56px;
    line-height: 1;
    letter-spacing: 1px;
    color: var(--brand-brown);
  }
  .contact {
    position: absolute;
    top: 182px;
    left: 0;
    width: 100%;
    text-align: center;
    font-style: normal;
    font-weight: 500;
    font-size: 14px;
    line-height: 18px;
    color: var(--ink);
  }
</style>
</head>
<body>
  <div class="letterhead">
    <svg class="top-band" viewBox="0 0 848 114" aria-hidden="true">
      <polygon points="0,0 848,0 848,103 424,0 0,113" fill="var(--brand-brown)"/>
    </svg>

    <div class="brand">
      <span class="brand-mark"></span>
      <span class="brand-name">BKA</span>
    </div>

    <address class="contact">
      <p class="contact-address">47 Fenbury Lane, Harlow Bay, ME 04231</p>
      <p class="contact-phone">555-481-7629</p>
    </address>
  </div>
</body>
</html>
```